Exciting new aperitif brand needs a great label

Vel-Orin is a wonderful rich new premium-priced bitter aperitif, with a deep red colour, from a 100+ year old distillery (1890) near Turin in the Piedmont region of Italy. Inspired by Torvesi, it is perfectly formulated to elevate the classic Baldetti cocktail (and variations on it). It also goes perfectly in a Spritz or a long mixed drink with soda or tonic. The name Vel-Orin is derived from the French for 'peak' and the Italian word for 'love'.

The label, which should take inspiration from Torvesi, but be distinctively different, can incoporate any number of premium label embellishments (foil, embossing, textures etc) and should be no greater than 11cm (height) x 9cm (width) with any core imagery restricted to a width of c.7cm.

The attached mood board should act as inspiration and colour should largely be restricted to reds, blues, whites and perhaps orange. For completeness, the label should note that the ABV is 25% and the bottle size 70cl.

Target Market(s)

21-45yr olds - equal split female/male

Colors
0054AA
0677BA
7BADD7
CADEEF
E8F1F8
0094D4
00A9DD
6FCCEA
C7EBF8
E9F6FB
EE7325
F08F49
F5BC92
FAE3D3
FDF4ED
EB3D1F
EC4F4E
F09395
F8D3D4
FCEDEE

Requirements
Must have
• Great lettering design on the name Vel-Orin

```html
<!DOCTYPE html>
<html lang="en">
<head>
<meta charset="utf-8">
<title>Vel-Orin Aperitif Label</title>
<link rel="stylesheet" href="https://fonts.googleapis.com/css2?family=Cinzel:wght@600&family=Exo+2:wght@500;600&display=swap">
<style>
  :root {
    --backdrop: #c4c4c4;
    --label-blue: #0054aa;
    --label-blue-deep: #0a4aa0;
    --label-white: #ffffff;
    --foil-gold: #d9962a;
    --foil-gold-light: #f0c060;
    --flower-light: #6fccea;
    --flower-mid: #0677ba;
    --flower-deep: #0d3f9e;
  }
  * { margin: 0; padding: 0; box-sizing: border-box; }
  html, body {
    width: 1200px;
    height: 2230px;
    overflow: hidden;
    background: var(--backdrop);
  }
  .canvas {
    position: relative;
    width: 1200px;
    height: 2230px;
  }
  .label {
    position: absolute;
    left: 100px;
    top: 501px;
    width: 1000px;
    height: 1227px;
  }
  .label-shape {
    position: absolute;
    inset: 0;
    width: 1000px;
    height: 1227px;
    filter: drop-shadow(0 6px 14px rgba(0,0,0,0.22));
  }
  .label-content {
    position: absolute;
    inset: 0;
    text-align: center;
  }
  .since {
    position: absolute;
    top: 178px;
    left: 0;
    right: 0;
    font-family: "Exo 2", sans-serif;
    font-weight: 600;
    font-size: 42px;
    letter-spacing: 2px;
    color: var(--foil-gold);
  }
  .brand-name {
    position: absolute;
    top: 300px;
    left: 0;
    right: 0;
    white-space: nowrap;
    font-family: "Cinzel", serif;
    font-weight: 600;
    font-size: 138px;
    letter-spacing: 8px;
    line-height: 1;
    color: var(--label-white);
  }
  .tagline {
    position: absolute;
    top: 512px;
    left: 0;
    right: 0;
    font-family: "Exo 2", sans-serif;
    font-weight: 600;
    font-size: 40px;
    color: var(--label-white);
    letter-spacing: 0.5px;
  }
  .tagline .divider {
    display: inline-block;
    width: 2px;
    height: 30px;
    background: var(--label-white);
    margin: 0 22px;
    vertical-align: -4px;
  }
  .volume {
    position: absolute;
    top: 1072px;
    left: 0;
    right: 0;
    font-family: "Exo 2", sans-serif;
    font-weight: 600;
    font-size: 60px;
    color: var(--label-blue);
  }
</style>
</head>
<body>
<div class="canvas">
  <div class="label">
    <svg class="label-shape" viewBox="0 0 1000 1227" xmlns="http://www.w3.org/2000/svg">
      <defs>
        <clipPath id="label-outline">
          <path d="M89,86 Q500,-86 911,86 A90,90 0 0 0 1000,167 L1000,1056 A90,90 0 0 0 911,1145 Q500,1309 89,1145 A90,90 0 0 0 0,1056 L0,167 A90,90 0 0 0 89,86 Z"/>
        </clipPath>
        <linearGradient id="blue-field" x1="0" y1="0" x2="0" y2="1">
          <stop offset="0" stop-color="var(--label-blue)"/>
          <stop offset="1" stop-color="var(--label-blue-deep)"/>
        </linearGradient>
        <linearGradient id="foil-band" x1="0" y1="0" x2="1" y2="0">
          <stop offset="0" stop-color="var(--foil-gold)"/>
          <stop offset="0.5" stop-color="var(--foil-gold-light)"/>
          <stop offset="1" stop-color="var(--foil-gold)"/>
        </linearGradient>
        <radialGradient id="flower-tone" cx="0.5" cy="0.5" r="0.5">
          <stop offset="0" stop-color="var(--flower-light)"/>
          <stop offset="0.55" stop-color="var(--flower-mid)"/>
          <stop offset="1" stop-color="var(--flower-deep)" stop-opacity="0.9"/>
        </radialGradient>
      </defs>
      <g clip-path="url(#label-outline)">
        <rect class="label-field" x="0" y="0" width="1000" height="1227" fill="url(#blue-field)"/>
        <path class="label-base-foil" d="M0,990 Q500,762 1000,990 L1000,1227 L0,1227 Z" fill="url(#foil-band)"/>
        <path class="label-base" d="M0,1002 Q500,776 1000,1002 L1000,1227 L0,1227 Z" fill="var(--label-white)"/>
      </g>
      <circle class="flower-emblem" cx="500" cy="849" r="115" fill="url(#flower-tone)" role="img" aria-label="Blue flower illustration"/>
    </svg>
    <div class="label-content">
      <p class="since">SINCE: 1890</p>
      <h1 class="brand-name">VEL-ORIN</h1>
      <p class="tagline">Premium Quality<span class="divider"></span>ABV is 25%</p>
      <p class="volume">70cl</p>
    </div>
  </div>
</div>
</body>
</html>
```